Branvique needs a business Card Design

We are looking for a business card Design for our new Managed Service Provider Company, Branvique. Branvique encompasses everything IT for the average medium sized business. Our primary services are help desk support, cyber-security (malware and ransomware protection), and Disaster Recovery systems. We would like the design to have a very clean and professional look, with a very minimalist feel.

Target Market(s)

Medium to large sized businesses

Industry/Entity Type

It Service

Contact Information for Business Card

Name GoesHere
name@branvique.com
O: 555-382-6047
C: 555-731-5820

Font styles to use
Other font styles liked:
• Poppins Font Only Please

Colors

Designer to choose only greyscale colors for use in the design.

Requirements
Must have
• Logo included
Nice to have
• Cutting Edge, innovative, minimalistic, elegant

```html
<!DOCTYPE html>
<html lang="en">
<head>
<meta charset="utf-8">
<title>Branvique – Business Card</title>
<link href="https://fonts.googleapis.com/css2?family=Poppins:wght@300;400;600&display=swap" rel="stylesheet">
<style>
  :root {
    --charcoal: #2b2b2b;
    --charcoal-deep: #1a1a1a;
    --charcoal-mid: #333333;
    --silver: #8f8f8f;
    --ink-grey: #727272;
    --paper: #ffffff;
    --stage: #e8e8e8;
  }
  * { margin: 0; padding: 0; box-sizing: border-box; }
  html, body {
    width: 1200px; height: 885px; overflow: hidden;
    background: var(--stage);
    font-family: "Poppins", sans-serif;
  }
  .stage {
    width: 1200px; height: 885px;
    display: flex; flex-direction: column;
    align-items: center; justify-content: space-evenly;
  }
  .card {
    width: 560px; height: 320px;
    position: relative;
    box-shadow: 0 10px 28px rgba(0,0,0,0.16);
  }
  .card--front { background: var(--paper); }
  .card--back {
    background: radial-gradient(ellipse at 55% 40%, var(--charcoal-mid) 0%, var(--charcoal-deep) 100%);
    display: flex; align-items: center; justify-content: center;
  }
  .brand-mark {
    position: absolute; top: 44px; right: 48px;
    display: flex; align-items: center; gap: 14px;
  }
  .brand-mark__square {
    width: 26px; height: 26px; background: var(--charcoal);
  }
  .brand-mark__name {
    font-weight: 600; font-size: 40px; color: var(--charcoal);
    letter-spacing: 0.01em; line-height: 1;
  }
  .contact-block {
    position: absolute; left: 48px; bottom: 40px;
    color: var(--charcoal);
  }
  .contact-block__name {
    font-weight: 600; font-size: 20px; letter-spacing: 0.01em; line-height: 1.1;
    text-transform: uppercase;
  }
  .contact-block__role {
    font-weight: 300; font-size: 15px; color: var(--ink-grey); margin-top: 2px;
  }
  .contact-list { list-style: none; margin-top: 18px; }
  .contact-list li {
    display: flex; align-items: center; gap: 9px;
    font-weight: 400; font-size: 15px; line-height: 1.55; color: var(--charcoal);
  }
  .contact-list svg { width: 12px; height: 12px; flex: none; }
  .back-wordmark {
    display: flex; align-items: center; gap: 18px;
  }
  .back-wordmark__square { width: 14px; height: 14px; background: var(--silver); }
  .back-wordmark__name {
    font-weight: 300; font-size: 26px; letter-spacing: 0.5em; color: var(--silver);
    text-transform: uppercase; margin-right: -0.5em;
  }
</style>
</head>
<body>
<main class="stage">
  <section class="card card--front" aria-label="Card front">
    <div class="brand-mark">
      <span class="brand-mark__square"></span>
      <span class="brand-mark__name">Branvique</span>
    </div>
    <div class="contact-block">
      <p class="contact-block__name">Dana Whitlock</p>
      <p class="contact-block__role">President</p>
      <ul class="contact-list">
        <li>
          <svg viewBox="0 0 12 12" aria-hidden="true"><path d="M2.5 1h2l1 3-1.5 1a6 6 0 0 0 3 3l1-1.5 3 1v2a1 1 0 0 1-1 1A9.5 9.5 0 0 1 1.5 2a1 1 0 0 1 1-1z" fill="currentColor"/></svg>
          555-382-6047
        </li>
        <li>
          <svg viewBox="0 0 12 12" aria-hidden="true"><rect x="3" y="0.8" width="6" height="10.4" rx="1" fill="none" stroke="currentColor" stroke-width="1.2"/><circle cx="6" cy="9.4" r="0.7" fill="currentColor"/></svg>
          555-731-5820
        </li>
        <li>
          <svg viewBox="0 0 12 12" aria-hidden="true"><rect x="0.8" y="2.5" width="10.4" height="7" fill="currentColor"/><path d="M1 3l5 3.5L11 3" fill="none" stroke="#fff" stroke-width="1"/></svg>
          name@branvique.com
        </li>
      </ul>
    </div>
  </section>

  <section class="card card--back" aria-label="Card back">
    <div class="back-wordmark">
      <span class="back-wordmark__square"></span>
      <span class="back-wordmark__name">Branvique</span>
    </div>
  </section>
</main>
</body>
</html>
```